Template design for micro site for a corporate-branded mobile software product

We need a creative web designer to help us quickly design a template design for a micro site webpage for a product called Varnello Unified Messaging, and we need the template design to be shown in 3 distinct industry designs. The template design shall be a one-page corporate brochure and product page, and the same template design will be re-used for 3 different industry pages. Although the layout and navigation design shall not change, each of the 3 industry pages must have its own unique design/content/look/feel to address specific capabilities of our product that are important to that industry or topic.

NOTE: This is a design project, not a web development project. We will hand your designs over to a web developer.

REQUIRED:
Create a template design that includes Varnello branding guidelines and can be used consistently for each of our 3 different industry micro site web pages (i.e., the template design should consider such things as overall page navigation design & layout design to deliver a common experience for the viewer).

REQUIRED:
In terms of layout, please model your template design after one of the following responsive website layouts, and please indicate which you chose:

http://www.themevault-example.com/gym-fitness-business-wordpress-theme-vigor/
http://www.themevault-example.com/blendo-a-sleek-flashy-and-professional-wordpress-theme/
http://www.themevault-example.com/bold-and-modern-responsive-business-wordpress-theme-brisko/
http://www.themevault-example.com/ledgerly-business-premium-wordpress-theme/
http://siteforge-example.org/themes/tailorix
http://www.themevault-example.com/plain-kit-business-portfolio-wordpress-theme/
http://www.themevault-example.com/stillwater-premium-origo-child-theme/

REQUIRED:
Use the template to design 3 unique designs, one for each of the following 3 industry topic pages (you may change anything in the design such as colors, pictures, icons, etc. to create a look/feel relevant for the topic):
- Workplace Harassment & HR
- Financial Institutions
- Mining & Construction (includes Oil, Gas, etc.)

Attached are content ideas for the above 3 industry topics for use in your suggested designs.

REQUIRED: Varnello branding is a requirement (we must use the spectrum design element at top of page). Colors can (probably should) change for each of the 3 micro site designs. You can see examples of Varnello branding at www.varnello-example.com, www.varnello-vum-example.com/school, and in the attached PowerPoints.

REQUIRED: We must have a contact us form similar to the form at the bottom of www.varnello-vum-example.com/school or at the bottom of www.pitchgallery-example.com. The specific goal of these 3 website designs are to drive sales leads and conversions to request more information from our sales team, so we are seeking a design/layout that helps drive site conversions.

REQUIRED: Navigation menu similar to the one at www.varnello-example.com (at the top of the page)

Nice to have:

PICTURES: Pictures will definitely need to change for each site. If you can make suggestions on pictures, that will help. We are ok with taking additional (optional) proposals if you find pictures you think really help the site.

Reason: We are looking for a design that really takes the Varnello branding guidelines into careful consideration.

We invite you to design your template based on one of the following responsive layouts, and please indicate to us which one you chose (so we can purchase it and give it to our web developer). Thank you.

Target Market(s)

Each of the 3 industry pages should target each of the following (respectively):
1. Workplace Harassment (general topic)
2. Financial Institutions (Banking, Insurance, Investment, Retail/Corporate)
3. Mining (includes Oil, Gas, and peripherally includes Energy)

See attached PowerPoint file for some content ideas for your design.

Industry/Entity Type

Software

Requirements
Must have
• - Templatte design must be modeled after one of the following layouts

- Template design must be a single page layout. Content should fit into screens of 1366x768, and no "scrolling" should be necessary if the user presses the navigation menu buttons (e.g., see www.varnello-vum-example.com/school for an example of how the navigation menu takes you to the content without scrolling)
- Each of the 3 micro site industry pages must be different (pictures, content, etc.) but must use the same template design
- Must use Varnello branding guidelines (attached)
- Must include a Contact Us form similar to the bottom of the page at www.varnello-vum-example.com/school or the bottom of the page at www.pitchgallery-example.com
- Must include a Navigation Bar at the top similar to www.varnello-example.com
- Must maintain some consistency (visually and navigation) with existing 2 micro sites already launched (see URLs above)
Nice to have
• - Pictures (it is ok to send a separate proposal for pictures if cost is a concern)
- Visual appeal with professional and modern look/feel
- Consideration for driving site conversions to "Getting Started" and "Request More Info" buttons
- Consideration for responsive web developer
- Consideration for SEO
Should not have
• - Search box

```html
<!DOCTYPE html>
<html lang="en">
<head>
<meta charset="utf-8">
<title>Workplace Harassment – Varnello Unified Messaging</title>
<link rel="stylesheet" href="https://fonts.googleapis.com/css2?family=Ubuntu:wght@300;400;500&family=Open+Sans:wght@400;600&display=swap">
<style>
:root{
  --purple:#8b2a8b;
  --purple-dark:#5e2a7e;
  --purple-mid:#742b88;
  --purple-light:#a8399a;
  --cyan:#14b3d6;
  --charcoal:#3a3a3c;
  --input:#5a5a5c;
  --pale:#f1f2f2;
  --white:#ffffff;
  --text:#555557;
  --logo:#8d8d8f;
  --logo-strong:#333335;
}
*{margin:0;padding:0;box-sizing:border-box}
html,body{width:1200px;height:2707px;overflow:hidden}
body{position:relative;font-family:"Open Sans",Arial,sans-serif;color:var(--text);background:var(--white)}

/* Hero */
.hero{position:absolute;left:0;top:0;width:1200px;height:670px;overflow:hidden}
.hero-photo{position:absolute;inset:0;background:linear-gradient(180deg,#eef0f1 0%,#d8d0c8 35%,#c3ada0 65%,#9c8a80 100%)}
.hero-bands{position:absolute;left:0;top:0}
.main-nav{position:absolute;top:36px;left:686px;display:flex;align-items:center;font-family:"Ubuntu",sans-serif;font-size:13px;text-transform:uppercase;color:#222}
.main-nav a{color:#222;text-decoration:none;margin-right:30px;height:38px;line-height:38px}
.main-nav a.active{background:var(--purple);color:var(--white);border-radius:8px;padding:0 18px;margin-right:36px}
.hero-title{position:absolute;left:189px;top:307px;width:819px;height:56px;background:var(--purple);color:var(--white);font-family:"Ubuntu",sans-serif;font-size:27px;font-weight:300;line-height:56px;text-align:center}
.btn{position:absolute;background:var(--cyan);color:var(--white);font-family:"Ubuntu",sans-serif;font-size:16px;text-align:center;text-decoration:none}
.hero-btn{left:532px;top:383px;width:138px;height:48px;line-height:48px}

/* Topics */
.topics{position:absolute;left:0;top:670px;width:1200px;height:381px;background:var(--charcoal);color:var(--white)}
.topic{position:absolute;width:260px;text-align:center}
.topic-icon{width:90px;height:90px;border-radius:50%;background:var(--purple);margin:0 auto;display:flex;align-items:center;justify-content:center}
.topic h3{font-family:"Ubuntu",sans-serif;font-weight:400;font-size:19px;margin-top:44px}
.topic p{font-size:12px;line-height:24px;margin-top:16px}

/* Intro */
.intro-text{position:absolute;left:150px;top:1100px;width:900px;text-align:center;font-family:"Ubuntu",sans-serif;font-weight:300;font-size:21px;line-height:40px;color:#5a5a5c;white-space:nowrap}
.intro-btn{left:530px;top:1254px;width:140px;height:46px;line-height:46px}
.rule{position:absolute;left:150px;top:1353px;width:900px;height:1px;background:#e6e6e6}
.feature{position:absolute;width:240px}
.feature-head{display:flex;align-items:center}
.feature-icon{width:40px;height:40px;background:var(--purple);display:flex;align-items:center;justify-content:center;margin-right:12px}
.feature h4{font-family:"Ubuntu",sans-serif;font-weight:400;font-size:18px;color:#4a4a4c}
.feature p{font-size:12px;line-height:22px;margin-top:18px;color:#6a6a6c;white-space:nowrap}

/* News */
.news{position:absolute;left:0;top:1620px;width:1200px;height:403px;background:var(--pale)}
.news-heading{position:absolute;left:150px;top:50px;width:900px;display:flex;align-items:center;font-family:"Ubuntu",sans-serif;font-size:19px;font-weight:400;color:#333}
.news-heading::before,.news-heading::after{content:"";flex:1;height:1px;background:#dcdcdc}
.news-heading span{padding:0 22px}
.news-item{position:absolute;top:106px;width:256px}
.news-item h5{font-family:"Ubuntu",sans-serif;font-weight:400;font-size:18px;color:#333;margin-bottom:36px}
.news-photo{width:256px;height:109px}
.news-item p{font-size:12px;line-height:21px;margin-top:24px;color:#555}
.news-item .more{display:block;font-size:13px;color:var(--purple);margin-top:8px;text-decoration:none}
.news-arrow{position:absolute;top:209px;width:22px;height:46px;border:1px solid #cfcfcf;background:var(--white);border-radius:11px;display:flex;align-items:center;justify-content:center}

/* Partners */
.partners{position:absolute;left:0;top:2023px;width:1200px;height:131px;background:var(--white)}
.partner{position:absolute;top:48px;transform:translateX(-50%);font-family:"Ubuntu",sans-serif;font-size:30px;font-weight:400;color:var(--logo);white-space:nowrap}
.partner.strong{color:var(--logo-strong)}

/* Footer */
.footer{position:absolute;left:0;top:2154px;width:1200px;height:553px;background:var(--charcoal);color:var(--white)}
.footer h6{position:absolute;font-family:"Ubuntu",sans-serif;font-weight:400;font-size:18px}
.contact-line{position:absolute;left:144px;display:flex;font-size:12px;line-height:16px}
.contact-line svg{margin-right:14px;flex:none}
.divider{position:absolute;left:395px;top:38px;width:1px;height:413px;background:#4c4c4e}
.field-label{position:absolute;font-size:12px;font-weight:600}
.field{position:absolute;background:var(--input)}
.submit{position:absolute;left:440px;top:411px;width:97px;height:40px;background:var(--purple);color:var(--white);font-size:13px;line-height:40px;text-align:center}
.footer-rule{position:absolute;left:144px;top:508px;width:912px;height:1px;background:#4c4c4e}
.footer-links{position:absolute;left:151px;top:524px;font-size:10px;color:#cfcfcf}
.footer-links a{color:#cfcfcf;text-decoration:none;margin-right:27px}
.copyright{position:absolute;right:144px;top:524px;font-size:10px;color:#cfcfcf}
</style>
</head>
<body>

<header class="hero">
  <div class="hero-photo" role="img" aria-label="Photo of a cheering group of office colleagues raising their arms"></div>
  <svg class="hero-bands" width="1200" height="670" viewBox="0 0 1200 670" aria-hidden="true">
    <polygon points="0,560 0,670 1200,670 1200,600 880,670 860,670" fill="var(--charcoal)"/>
    <polygon points="0,455 520,560 860,670 0,585" fill="var(--purple-light)"/>
    <polygon points="0,520 860,670 0,610" fill="var(--purple-dark)"/>
    <polygon points="0,585 860,670 0,660" fill="var(--purple)"/>
    <polygon points="300,490 860,670 620,560" fill="var(--purple-mid)"/>
    <polygon points="1200,440 1200,520 900,670 870,670" fill="var(--purple)"/>
    <polygon points="1200,520 1200,600 900,670" fill="var(--purple-dark)"/>
    <polygon points="1200,395 1200,445 880,670" fill="var(--purple-light)"/>
  </svg>
  <nav class="main-nav">
    <a class="active" href="#">Home</a>
    <a href="#">Services</a>
    <a href="#">Clients</a>
    <a href="#">The Team</a>
    <a href="#">Contact</a>
  </nav>
  <h1 class="hero-title">This is a Workplace Harassment website design theme for purchase</h1>
  <a class="btn hero-btn" href="#">Read more</a>
</header>

<section class="topics">
  <div class="topic" style="left:132px;top:81px">
    <div class="topic-icon">
      <svg width="44" height="40" viewBox="0 0 44 40"><rect x="3" y="3" width="38" height="25" rx="2" fill="none" stroke="#fff" stroke-width="4"/><rect x="18" y="28" width="8" height="6" fill="#fff"/><rect x="11" y="34" width="22" height="4" fill="#fff"/></svg>
    </div>
    <h3>Cyber stalking</h3>
    <p>Lorem ipsum dolor sit erat amet, sect tur adipiscing elit. Sed rhoncus elit erat lorem ipsum faucibus</p>
  </div>
  <div class="topic" style="left:470px;top:81px">
    <div class="topic-icon">
      <svg width="48" height="44" viewBox="0 0 48 44" fill="#fff"><circle cx="24" cy="10" r="6"/><path d="M16 20h16v16h-4v8h-8v-8h-4z"/><circle cx="9" cy="15" r="4"/><path d="M3 23h12v12H3z"/><circle cx="39" cy="15" r="4"/><path d="M33 23h12v12H33z"/></svg>
    </div>
    <h3>Bullying</h3>
    <p>Lorem ipsum dolor sit erat amet, sect tur adipiscing elit. Sed rhoncus elit erat lorem ipsum faucibus</p>
  </div>
  <div class="topic" style="left:808px;top:81px">
    <div class="topic-icon">
      <svg width="48" height="42" viewBox="0 0 48 42" fill="#fff"><circle cx="30" cy="12" r="10"/><path d="M12 42c0-12 8-18 18-18s18 6 18 18z"/><circle cx="14" cy="16" r="7" stroke="var(--purple)" stroke-width="2"/><path d="M0 42c0-9 6-14 14-14s14 5 14 14z" stroke="var(--purple)" stroke-width="2"/></svg>
    </div>
    <h3>Sexual harassment</h3>
    <p>Lorem ipsum dolor sit erat amet, sect tur adipiscing elit. Sed rhoncus elit erat lorem ipsum faucibus</p>
  </div>
</section>

<section class="intro">
  <p class="intro-text">Lorem ipsum dolor sit amet, consectetur adipiscing elit. Sed rhoncus faucibus fau-<br>cibus. Maecenas erat odio, mattis id suscipit a, ullamcorper nec felis. Pellentesque<br>ut sem et ante condimentum ultrices quis nec lorem.</p>
  <a class="btn intro-btn" href="#">Read more</a>
  <div class="rule"></div>

  <div class="feature" style="left:153px;top:1403px">
    <div class="feature-head"><div class="feature-icon"><svg width="22" height="22" viewBox="0 0 22 22"><path d="M4 18l3-7 9-9 4 4-9 9z" fill="#fff"/><path d="M2 20l3-3" stroke="#fff" stroke-width="2"/></svg></div><h4>Lorem ipsum dolor</h4></div>
    <p>Lorem ipsum dolor sit amet, con-<br>sectetur adipiscing elit. Sed rhoncus<br>faucibus faucibus. Maecenas erat odio,<br>mattis id suscipit a, ullamcorper nec<br>felis. Pellentesque ut sem et.</p>
  </div>
  <div class="feature" style="left:496px;top:1403px">
    <div class="feature-head"><div class="feature-icon"><svg width="22" height="22" viewBox="0 0 22 22"><path d="M4 18l3-7 9-9 4 4-9 9z" fill="#fff"/><path d="M2 20l3-3" stroke="#fff" stroke-width="2"/></svg></div><h4>Lorem ipsum dolor</h4></div>
    <p>Lorem ipsum dolor sit amet, con-<br>sectetur adipiscing elit. Sed rhoncus<br>faucibus faucibus. Maecenas erat odio,<br>mattis id suscipit a, ullamcorper nec<br>felis. Pellentesque ut sem et.</p>
  </div>
  <div class="feature" style="left:826px;top:1403px">
    <div class="feature-head"><div class="feature-icon"><svg width="22" height="22" viewBox="0 0 22 22"><path d="M4 18l3-7 9-9 4 4-9 9z" fill="#fff"/><path d="M2 20l3-3" stroke="#fff" stroke-width="2"/></svg></div><h4>Lorem ipsum dolor</h4></div>
    <p>Lorem ipsum dolor sit amet, con-<br>sectetur adipiscing elit. Sed rhoncus<br>faucibus faucibus. Maecenas erat odio,<br>mattis id suscipit a, ullamcorper nec<br>felis. Pellentesque ut sem et.</p>
  </div>
</section>

<section class="news">
  <h2 class="news-heading"><span>Latest news</span></h2>
  <div class="news-arrow" style="left:106px"><svg width="8" height="12" viewBox="0 0 8 12"><path d="M7 1L2 6l5 5" fill="none" stroke="#555" stroke-width="2"/></svg></div>
  <article class="news-item" style="left:156px">
    <h5>Latest news topic one</h5>
    <div class="news-photo" role="img" aria-label="Photo of three business people in suits" style="background:linear-gradient(90deg,#e8e8e8,#6a6a6a 30%,#9a9a9a 50%,#4a4a4a 75%,#e8e8e8)"></div>
    <p>Lorem ipsum dolor sit arenet, consectetur adipiscing elit. Sed rhoncus faucibus.</p>
    <a class="more" href="#">more</a>
  </article>
  <article class="news-item" style="left:469px">
    <h5>Latest news topic two</h5>
    <div class="news-photo" role="img" aria-label="Photo of a hand using a tablet on a desk" style="background:linear-gradient(120deg,#b9b2a6,#e4e6e2 45%,#a8b8c2 70%,#d8d4cc)"></div>
    <p>Lorem ipsum dolor sit arenet, consectetur adipiscing elit. Sed rhoncus faucibus.</p>
    <a class="more" href="#">more</a>
  </article>
  <article class="news-item" style="left:790px">
    <h5>Latest news topic three</h5>
    <div class="news-photo" role="img" aria-label="Photo of a business team standing in a row" style="background:linear-gradient(180deg,#dfe3e6,#7c8088 55%,#3e4048)"></div>
    <p>Lorem ipsum dolor sit arenet, consectetur adipiscing elit. Sed rhoncus faucibus.</p>
    <a class="more" href="#">more</a>
  </article>
  <div class="news-arrow" style="left:1069px"><svg width="8" height="12" viewBox="0 0 8 12"><path d="M1 1l5 5-5 5" fill="none" stroke="#555" stroke-width="2"/></svg></div>
</section>

<section class="partners">
  <span class="partner" style="left:204px">Norvale</span>
  <span class="partner" style="left:355px">Quadrix</span>
  <span class="partner" style="left:505px">KESTREL</span>
  <span class="partner" style="left:673px">Brightwell</span>
  <span class="partner strong" style="left:843px">TORVIK</span>
  <span class="partner" style="left:997px">Quadrix</span>
</section>

<footer class="footer">
  <h6 style="left:144px;top:42px">Contacts</h6>
  <div class="contact-line" style="top:104px">
    <svg width="14" height="18" viewBox="0 0 14 18"><rect x="2" y="1" width="10" height="16" rx="2" fill="none" stroke="#fff" stroke-width="2"/></svg>
    <span>1800-5550-1234</span>
  </div>
  <div class="contact-line" style="top:143px">
    <svg width="14" height="14" viewBox="0 0 14 14"><rect x="1" y="2" width="12" height="8" fill="none" stroke="#fff" stroke-width="1.6"/><rect x="4" y="11" width="6" height="2" fill="#fff"/></svg>
    <span>info@company-example.com</span>
  </div>
  <div class="contact-line" style="top:184px">
    <svg width="14" height="14" viewBox="0 0 14 14"><path d="M7 1l6 6h-2v6H3V7H1z" fill="#fff"/></svg>
    <span>54 Elm Row<br>Harlow Court, Elmstead Building<br>Northgate State<br>NG0098</span>
  </div>
  <div class="divider"></div>

  <h6 style="left:440px;top:42px">Get in touch</h6>
  <span class="field-label" style="left:440px;top:98px">Name</span>
  <div class="field" style="left:440px;top:124px;width:298px;height:36px"></div>
  <span class="field-label" style="left:756px;top:98px">Your email</span>
  <div class="field" style="left:756px;top:124px;width:295px;height:36px"></div>
  <span class="field-label" style="left:440px;top:182px">Your message</span>
  <div class="field" style="left:440px;top:208px;width:611px;height:180px"></div>
  <div class="submit">Submit</div>

  <div class="footer-rule"></div>
  <nav class="footer-links"><a href="#">Home</a><a href="#">Contact Us</a><a href="#">Privacy Policy</a></nav>
  <span class="copyright">Company.&nbsp; Copyright 2013.&nbsp; All rights reserved</span>
</footer>

</body>
</html>
```